Bramfield Animal Hospital brochure

We have found that our current clients do not know all of the services that we offer so we want to make a hospital brochure to make our services more known. Our website has all of our services listed but we find that clients aren't looking at our website as much as we would like so we are hoping a hospital brochure can sum up our main services and maybe lead to more people visiting our website. Our hospital colors are blue and maroon and our moto is "Outstanding Medicine, Extraordinary Service." Some of the service we would like to promote more include digital x-ray, ultrasounds, echocardiograms, laser therapy and dentals. We also offer after hours emergency care but only to our current clients. You can find more services listed on our website We are in a small town so we want a personal yet professional feel.

Feel free to visit our website to get a better feel for our business https://thecorvelpets.com/

• 6-8 panel brochure
• I included some photos from around the hospital. If you feel that you can make a few work in the brochure then great but don't feel obligated to.

```html
<!DOCTYPE html>
<html lang="en">
<head>
<meta charset="utf-8">
<title>Bramfield Animal Hospital – Services Brochure</title>
<link rel="stylesheet" href="https://fonts.googleapis.com/css2?family=Montserrat:wght@400;500;600;700;800&display=swap">
<style>
  :root {
    --maroon: #9a1c20;
    --maroon-dark: #7d1417;
    --navy: #1d2b4f;
    --ink: #2b2b2b;
    --paper: #ffffff;
    --paper-warm: #f4f4f2;
    --stage: #e4e4e7;
    --rule: #cfcfd4;
  }
  * { box-sizing: border-box; margin: 0; padding: 0; }
  html, body { width: 1200px; height: 3268px; overflow: hidden; }
  body {
    position: relative;
    background: var(--stage);
    font-family: "Montserrat", Arial, sans-serif;
    color: var(--ink);
  }
  .spread { position: absolute; left: 80px; width: 1040px; height: 740px; }
  .page {
    position: absolute; top: 0; width: 520px; height: 740px;
    background: var(--paper); overflow: hidden;
    box-shadow: 0 14px 30px rgba(0,0,0,.12);
  }
  .page--left { left: 0; }
  .page--right { left: 520px; box-shadow: 0 14px 30px rgba(0,0,0,.12), inset 8px 0 14px -10px rgba(0,0,0,.18); }
  .photo { position: absolute; }

  /* back cover */
  .back { background: var(--paper-warm); }
  .back__inner { position: absolute; top: 150px; left: 0; width: 100%; text-align: center; }
  .brand-name { font-weight: 700; color: var(--maroon); font-size: 15px; letter-spacing: .06em; text-transform: uppercase; line-height: 1.35; }
  .contact__title { margin-top: 26px; font-weight: 800; color: var(--navy); font-size: 30px; letter-spacing: .01em; }
  .contact__list { list-style: none; margin-top: 22px; }
  .contact__item { margin-bottom: 16px; font-weight: 600; font-size: 15px; color: var(--ink); line-height: 1.3; }
  .contact__item svg { display: block; margin: 0 auto 5px; }
  .contact__web { font-weight: 700; }

  /* front cover */
  .cover__photo { left: 24px; top: 50px; width: 472px; height: 530px;
    background: linear-gradient(180deg, #25331f 0%, #3e4a34 45%, #8b7a5e 75%, #b9a27a 100%); }
  .cover__badge { position: absolute; left: 282px; top: 38px; width: 190px; height: 112px; border-radius: 50%;
    background: var(--paper); display: flex; align-items: center; justify-content: center; text-align: center; }
  .cover__badge .brand-name { font-size: 13px; }
  .cover__band { position: absolute; left: 24px; top: 530px; width: 472px; height: 86px; background: var(--maroon);
    color: #fff; text-align: center; display: flex; flex-direction: column; justify-content: center; }
  .cover__motto-1 { font-size: 22px; font-weight: 600; letter-spacing: .06em; }
  .cover__motto-2 { font-size: 25px; font-weight: 800; letter-spacing: .05em; }
  .cover__web { position: absolute; top: 652px; width: 100%; text-align: center; color: var(--navy); font-weight: 700; font-size: 20px; letter-spacing: .03em; }

  /* inner pages */
  .hero { left: 0; top: 0; width: 1040px; height: 300px; z-index: 2;
    background: linear-gradient(180deg, #0f140d 0%, #223619 40%, #4f8f2e 70%, #6cb23a 100%); }
  .service-photo { box-shadow: 0 6px 14px rgba(0,0,0,.25); border: 6px solid #fff; }
  .service-card { position: absolute; background: #fff; padding: 22px 22px 20px; box-shadow: 0 6px 16px rgba(0,0,0,.18); }
  .service-card__title { color: var(--maroon); font-weight: 700; font-size: 18px; margin-bottom: 10px; }
  .service-card__text { font-size: 11.5px; line-height: 1.65; color: #333; }

  .page-foot { position: absolute; left: 0; bottom: 0; width: 100%; height: 60px; }
  .page-foot__mark { position: absolute; left: 24px; bottom: 26px; font-size: 7px; font-weight: 700; color: var(--maroon); text-transform: uppercase; letter-spacing: .05em; }
  .page-foot__rule { position: absolute; left: 24px; right: 24px; bottom: 20px; height: 1px; background: var(--rule); }
  .page-foot__web { position: absolute; right: 54px; bottom: 14px; background: var(--maroon); color: #fff; font-size: 8.5px; font-weight: 600; padding: 3px 12px; border-radius: 10px 0 0 10px; }
  .page-foot__num { position: absolute; right: 24px; bottom: 10px; width: 24px; height: 24px; border-radius: 50%; background: #fff; border: 1px solid var(--rule); font-size: 9px; font-weight: 700; color: var(--navy); display: flex; align-items: center; justify-content: center; }
</style>
</head>
<body>

<!-- Outer spread: back cover + front cover -->
<section class="spread" style="top:60px">
  <article class="page page--left back">
    <div class="back__inner">
      <p class="brand-name">Bramfield<br>Animal Hospital</p>
      <h2 class="contact__title">CONTACT US</h2>
      <ul class="contact__list">
        <li class="contact__item">
          <svg width="16" height="16" viewBox="0 0 24 24"><path fill="#9a1c20" d="M6.6 10.8a15.2 15.2 0 0 0 6.6 6.6l2.2-2.2a1 1 0 0 1 1-.25 11.4 11.4 0 0 0 3.6.57 1 1 0 0 1 1 1V20a1 1 0 0 1-1 1A17 17 0 0 1 3 4a1 1 0 0 1 1-1h3.5a1 1 0 0 1 1 1c0 1.25.2 2.45.57 3.57a1 1 0 0 1-.25 1z"/></svg>
          555-014-2271
        </li>
        <li class="contact__item">
          <svg width="16" height="16" viewBox="0 0 24 24"><rect x="4" y="8" width="16" height="12" rx="1.5" fill="#9a1c20"/><rect x="7" y="3" width="10" height="6" fill="#9a1c20"/><rect x="7" y="13" width="10" height="4" fill="#fff"/></svg>
          555-014-3380
        </li>
        <li class="contact__item">
          <svg width="16" height="14" viewBox="0 0 24 20"><rect x="1" y="2" width="22" height="16" rx="2" fill="#9a1c20"/><path d="M2 4l10 7 10-7" stroke="#fff" stroke-width="1.8" fill="none"/></svg>
          info@thecorvelpets.com
        </li>
        <li class="contact__item">
          <svg width="14" height="18" viewBox="0 0 24 30"><path fill="#9a1c20" d="M12 0a10 10 0 0 0-10 10c0 7.5 10 20 10 20s10-12.5 10-20A10 10 0 0 0 12 0z"/><circle cx="12" cy="10" r="4" fill="#fff"/></svg>
          Bramfield Animal Hospital<br>48 Maple Ridge Road<br>Bramfield, Vermont, 05399
        </li>
        <li class="contact__item contact__web">
          <svg width="16" height="16" viewBox="0 0 24 24"><circle cx="12" cy="12" r="10" fill="#9a1c20"/><path d="M2 12h20M12 2c3 3 3 17 0 20M12 2c-3 3-3 17 0 20" stroke="#fff" stroke-width="1.4" fill="none"/></svg>
          www.thecorvelpets.com
        </li>
      </ul>
    </div>
  </article>
  <article class="page page--right">
    <div class="photo cover__photo" role="img" aria-label="Veterinarian kneeling outdoors with two small dogs in front of evergreen trees"></div>
    <div class="cover__badge"><p class="brand-name">Bramfield<br>Animal Hospital</p></div>
    <div class="cover__band">
      <p class="cover__motto-1">OUTSTANDING MEDICINE,</p>
      <p class="cover__motto-2">EXTRAORDINARY SERVICE.</p>
    </div>
    <p class="cover__web">www.thecorvelpets.com</p>
  </article>
</section>

<!-- Inner spread 1: Digital X-Ray + Ultrasounds -->
<section class="spread" style="top:862px">
  <article class="page page--left">
    <div class="photo service-photo" style="left:22px;top:320px;width:210px;height:250px;background:linear-gradient(160deg,#3b4252,#6d7280 60%,#a7a9b0);" role="img" aria-label="Staff positioning a pet on the x-ray table"></div>
    <div class="service-card" style="left:210px;top:360px;width:285px;">
      <h3 class="service-card__title">Digital X-Ray</h3>
      <p class="service-card__text">Our digital x-ray system gives us clear images within minutes, so we can find broken bones, swallowed objects and changes in the heart, lungs and belly quickly. Less time under the machine means less stress for your pet, and images can be shared with specialists whenever a second opinion is helpful.</p>
    </div>
    <div class="page-foot"><span class="page-foot__mark">Bramfield Animal Hospital</span><span class="page-foot__rule"></span><span class="page-foot__web">www.thecorvelpets.com</span><span class="page-foot__num">01</span></div>
  </article>
  <article class="page page--right">
    <div class="photo service-photo" style="left:24px;top:320px;width:220px;height:250px;background:linear-gradient(160deg,#d7d9dc,#9b9fa6 55%,#5b5f66);" role="img" aria-label="Technician performing an ultrasound on a cat"></div>
    <div class="service-card" style="left:225px;top:360px;width:272px;">
      <h3 class="service-card__title">Ultrasounds</h3>
      <p class="service-card__text">An ultrasound is a pain-free, non-invasive way to look inside the body using sound waves. It lets us study the size, shape and texture of organs such as the liver, kidneys and bladder in real time. Most pets need no sedation, and results are often ready during the same visit.</p>
    </div>
    <div class="page-foot"><span class="page-foot__mark">Bramfield Animal Hospital</span><span class="page-foot__rule"></span><span class="page-foot__web">www.thecorvelpets.com</span><span class="page-foot__num">02</span></div>
  </article>
  <div class="photo hero" role="img" aria-label="Two small terriers playing on green grass"></div>
</section>

<!-- Inner spread 2: Echocardiograms + Laser therapy -->
<section class="spread" style="top:1664px">
  <article class="page page--left">
    <div class="photo service-photo" style="left:22px;top:36px;width:220px;height:570px;background:linear-gradient(180deg,#2c3440,#4b5663 40%,#7d6a58 80%,#2b2520);" role="img" aria-label="Echocardiogram monitor showing a heart scan beside a patient"></div>
    <div class="service-card" style="left:205px;top:110px;width:290px;">
      <h3 class="service-card__title">Echocardiograms</h3>
      <p class="service-card__text">An echocardiogram is an ultrasound of the heart. It shows us how each chamber and valve moves with every beat and how well blood flows through them. It helps us find heart disease early, plan the right medication and follow your pet's progress over time, all without needles or surgery.</p>
    </div>
    <div class="page-foot"><span class="page-foot__mark">Bramfield Animal Hospital</span><span class="page-foot__rule"></span><span class="page-foot__web">www.thecorvelpets.com</span><span class="page-foot__num">03</span></div>
  </article>
  <article class="page page--right">
    <div class="photo service-photo" style="left:272px;top:36px;width:226px;height:570px;background:radial-gradient(circle at 55% 62%,#e0312b 0%,#8d1512 18%,#3a0c0b 45%,#1a0707 100%);" role="img" aria-label="Red laser beam in a dark treatment room"></div>
    <div class="service-card" style="left:28px;top:150px;width:272px;">
      <h3 class="service-card__title">Laser therapy</h3>
      <p class="service-card__text">Cold laser therapy uses gentle light to ease pain, calm swelling and speed healing. It is a drug-free option for arthritis, wounds, sprains and recovery after surgery. Sessions take only minutes, most pets relax during treatment, and many owners notice an easier stride after just a few visits.</p>
    </div>
    <div class="page-foot"><span class="page-foot__mark">Bramfield Animal Hospital</span><span class="page-foot__rule"></span><span class="page-foot__web">www.thecorvelpets.com</span><span class="page-foot__num">04</span></div>
  </article>
</section>

<!-- Inner spread 3: Dental Care + Emergency Care -->
<section class="spread" style="top:2466px">
  <article class="page page--left">
    <div class="photo service-photo" style="left:22px;top:36px;width:220px;height:570px;background:linear-gradient(180deg,#3a3d52,#a97a45 35%,#d9c3a0 70%,#5a4a3a);" role="img" aria-label="Two dogs resting together in the hospital"></div>
    <div class="service-card" style="left:205px;top:110px;width:290px;">
      <h3 class="service-card__title">Dental Care</h3>
      <p class="service-card__text">Healthy teeth mean a healthier pet. Our dental cleanings include a full exam, scaling above and below the gum line, polishing and dental x-rays to spot problems hidden from view. We monitor every patient closely under anesthesia and send you home with tips for brushing and daily care.</p>
    </div>
    <div class="page-foot"><span class="page-foot__mark">Bramfield Animal Hospital</span><span class="page-foot__rule"></span><span class="page-foot__web">www.thecorvelpets.com</span><span class="page-foot__num">05</span></div>
  </article>
  <article class="page page--right">
    <div class="photo service-photo" style="left:272px;top:36px;width:226px;height:570px;background:linear-gradient(160deg,#1a1410,#4a2f1c 40%,#8a5a32 65%,#1e1712);" role="img" aria-label="Close view of a brown dog in low light"></div>
    <div class="service-card" style="left:28px;top:170px;width:272px;">
      <h3 class="service-card__title">Emergency Care</h3>
      <p class="service-card__text">Emergencies are unpredictable and often stressful. For our current clients, we offer after-hours emergency care so help is only a phone call away. Call the main number and follow the prompts to reach the doctor on call, who will guide you on what to do next.</p>
    </div>
    <div class="page-foot"><span class="page-foot__mark">Bramfield Animal Hospital</span><span class="page-foot__rule"></span><span class="page-foot__web">www.thecorvelpets.com</span><span class="page-foot__num">06</span></div>
  </article>
</section>

</body>
</html>
```